New business card for a regional office of a US M&A company

We need business card for a finance company, office based in Hong Kong , our Head office is in US, our business is to Merge and acquires companies , the new office will be a regional office for the Asia Pacific region. We want to use the head office logo as attached ( but don't have to be exactly the same, can be a variation to it) as a base and then add Asia Pacific alongside the logo.
We would prefer to have be bilingual Eng + Chinese, although we don't really have Chinese company name .

Industry/Entity Type

Business

Contact Information for Business Card

Clara Ruth Lindqvist
 

VP,
APAC M&A Operations
Oran Meridian Asia Pacific Limited
 
Unit 1807, K28
14 Tai Lok Fung Road, 
Hong Kong 
 
M: +852 6418 2074
T : +852 2836 4100
F : +852 2836 4177
VOIP: 4815
 
crlindqvist@oranmeridian.com

Font styles to use
Serif
Sans Serif

Colors

Designer to choose colors to be used in the design.

Requirements
Must have
• APAC Office

```html
<!DOCTYPE html>
<html lang="en">
<head>
<meta charset="utf-8">
<title>Oran Meridian Asia Pacific – Business Card</title>
<link href="https://fonts.googleapis.com/css2?family=Open+Sans:wght@400;600;700;800&display=swap" rel="stylesheet">
<style>
  :root {
    --bg: #111111;
    --card-white: #ffffff;
    --navy: #16263f;
    --navy-deep: #0f2740;
    --navy-light: #1d3752;
    --accent: #29a8d3;
    --text-grey: #555b63;
    --text-soft: #6b7178;
  }
  * { margin: 0; padding: 0; box-sizing: border-box; }
  html, body {
    width: 1200px; height: 1000px; overflow: hidden;
    background: var(--bg);
    font-family: "Open Sans", Arial, sans-serif;
  }
  .stage { position: relative; width: 1200px; height: 1000px; }

  .card {
    position: absolute;
    width: 525px; height: 300px;
    border-radius: 22px;
    overflow: hidden;
  }

  /* Front */
  .card-front {
    left: 70px; top: 200px;
    background: var(--card-white);
  }
  .card-front .accent-band {
    position: absolute; left: 0; right: 0; bottom: 0;
    height: 16px; background: var(--accent);
  }
  .holder-name {
    position: absolute; left: 34px; top: 32px;
    font-size: 27px; font-weight: 700; color: var(--navy);
    letter-spacing: -0.2px;
  }
  .holder-title {
    position: absolute; left: 35px; top: 70px;
    font-size: 13px; color: var(--text-soft);
  }
  .contact-list {
    position: absolute; left: 34px; top: 128px;
    list-style: none;
  }
  .contact-list li {
    display: flex; align-items: center; gap: 10px;
    font-size: 14px; color: var(--text-grey);
    height: 22px;
  }
  .contact-list svg { width: 13px; height: 13px; flex: none; }
  .voip {
    position: absolute; right: 36px; top: 150px;
    font-size: 14px; font-weight: 600; color: var(--accent);
  }
  .address {
    position: absolute; right: 36px; bottom: 40px;
    text-align: right; font-style: normal;
    font-size: 15px; line-height: 21px; color: var(--text-grey);
  }

  /* Back */
  .card-back {
    left: 605px; top: 500px;
    background: linear-gradient(135deg, var(--navy-light) 0%, var(--navy-deep) 100%);
    display: flex; flex-direction: column; align-items: center; justify-content: center;
  }
  .brand-square {
    width: 40px; height: 40px;
    border: 5px solid var(--card-white);
    margin-bottom: 14px;
  }
  .brand-name {
    font-size: 40px; font-weight: 800; color: var(--accent);
    letter-spacing: 1px; line-height: 1;
  }
  .brand-region {
    margin-top: 6px;
    font-size: 17px; font-weight: 700; color: var(--card-white);
  }
</style>
</head>
<body>
<main class="stage">

  <section class="card card-front" aria-label="Business card front">
    <h1 class="holder-name">Clara Ruth Lindqvist</h1>
    <p class="holder-title">VP, APAC M&amp;A Operations</p>

    <ul class="contact-list">
      <li>
        <svg viewBox="0 0 13 13" aria-hidden="true"><rect x="3" y="0.5" width="7" height="12" rx="1.2" fill="none" stroke="#29a8d3" stroke-width="1.3"/><line x1="5.5" y1="10.5" x2="7.5" y2="10.5" stroke="#29a8d3" stroke-width="1.2"/></svg>
        +852 6418 2074
      </li>
      <li>
        <svg viewBox="0 0 13 13" aria-hidden="true"><path d="M3 1 L5 1 L6 4 L4.5 5 Q5.5 7.5 8 8.5 L9 7 L12 8 L12 10 Q11 12 9 12 Q2 10 1 3 Q1 1 3 1 Z" fill="#29a8d3"/></svg>
        +852 2836 4100
      </li>
      <li>
        <svg viewBox="0 0 13 13" aria-hidden="true"><rect x="3" y="1" width="7" height="4" fill="#29a8d3"/><rect x="1" y="5" width="11" height="6" rx="1" fill="#29a8d3"/><rect x="3.5" y="7" width="6" height="1.3" fill="#fff"/></svg>
        +852 2836 4177
      </li>
      <li>
        <svg viewBox="0 0 13 13" aria-hidden="true"><rect x="0.5" y="2.5" width="12" height="8" fill="#29a8d3"/><path d="M0.8 2.8 L6.5 7 L12.2 2.8" fill="none" stroke="#fff" stroke-width="1.1"/></svg>
        crlindqvist@oranmeridian.com
      </li>
    </ul>

    <p class="voip">VOIP: 4815</p>

    <address class="address">
      Unit 1807, K28<br>
      14 Tai Lok Fung Road<br>
      Hong Kong
    </address>

    <div class="accent-band"></div>
  </section>

  <section class="card card-back" aria-label="Business card back">
    <div class="brand-square" aria-hidden="true"></div>
    <p class="brand-name">ORAN MERIDIAN</p>
    <p class="brand-region">Asia Pacific LTD</p>
  </section>

</main>
</body>
</html>
```